Book Cover design - Book Series about Animal Assisted Interventions need Book cover design -

Name of First Book - Open Paths - Your Early Days with Therapy Companion Programmes, by Dr Harriet Pembury. We are seeking an emotive, symbolic, and cohesive cover design for The Kindle Series – a ten-part book collection exploring the therapeutic power of animals in education, care, therapy, and professional growth. The series is written by the founder of Marrowdene, a UK-based therapeutic organisation that works with over 30 species to support children, families, and professionals.

The design should reflect the heart-led, reflective, and transformative nature of the series. Core themes include emotional connection, healing, purpose, courage, and growth. Each book will focus on a specific theme or species (e.g. dogs, llamas, leadership, burnout, personal growth) but should visually connect as part of a unified collection.

Key design elements:

(Open to suggestions however currently leaning on - ) not essential - feel free to try other things - probably Deep purple background as the grounding colour

Warm orange for accents (energy, hope) (again open to suggestions - different designs)

possibly Black or white silhouettes for symbolic human–animal imagery.. BUT OPEN ALL DIFFERENT DESIGNS!

Please don't use the actual Logos on the design, but it would be good if there was some theme that resonates them together - like style/colour

Clean, elegant typography (with “KINDLE” as the visual anchor in every title)

Symbolism encouraged (paths, hearts, trees, circles, rising suns). I like the ones where a human is touching calmly with an animal, either looking at each other, walking together, sitting together etc.. Vulnerable people is often more powerful (like children or older people)

Visual “nod” to the Marrowdene brand style – soft curves, emotional tone, nature-inspired calm

Designers are invited to submit a concept for the books with some finished designs. Each cover should stand alone while fitting beautifully into a recognisable series.

Target Market(s)

Teachers, therapists, professionals, adults, mature adults, Mature students

Industry/Entity Type

Therapy, education, animal work, pet therapy

Font styles to use
Sans Serif

Colors

Designer to choose colors to be used in the design.

Requirements
Must have
• Deep emotion, calm, intrigue,
Nice to have
• Deep colours, features of animals and people, Book title, Author name - Harriet Pembury
Should not have
• Not be childish/for children

```html
<!DOCTYPE html>
<html lang="en">
<head>
<meta charset="utf-8">
<title>Open Paths – Dr Harriet Pembury</title>
<link href="https://fonts.googleapis.com/css2?family=Bebas+Neue&family=Poppins:wght@300;400;600&display=swap" rel="stylesheet">
<style>
  :root {
    --paper: #ffffff;
    --plum-deep: #3a0550;
    --plum: #5b0a86;
    --violet: #8c0089;
    --magenta: #b0218c;
    --coral: #e0483a;
    --orange: #ff6a00;
    --amber: #ff8a00;
    --ink-light: #ffffff;
  }
  * { margin: 0; padding: 0; box-sizing: border-box; }
  html, body { width: 800px; height: 1200px; overflow: hidden; background: var(--paper); }
  .cover {
    position: relative;
    width: 800px;
    height: 1200px;
    background: var(--paper);
    overflow: hidden;
  }
  .series-band {
    position: absolute;
    left: 53px; top: 40px;
    width: 697px; height: 47px;
    background: linear-gradient(90deg, var(--plum), var(--plum-deep));
    color: var(--ink-light);
    font-family: "Bebas Neue", sans-serif;
    font-size: 30px;
    letter-spacing: 2.2px;
    display: flex; align-items: center; justify-content: center;
    padding-top: 3px;
    white-space: nowrap;
  }
  .title { font-weight: normal; }
  .title-lead {
    position: absolute;
    left: 53px; top: 96px;
    width: 697px;
    font-family: "Poppins", sans-serif;
    font-weight: 300;
    font-size: 114px;
    line-height: 1;
    color: var(--plum-deep);
    display: flex; justify-content: space-between;
  }
  .title-anchor {
    position: absolute;
    left: 60px; top: 196px;
    width: 680px;
    font-family: "Bebas Neue", sans-serif;
    font-size: 350px;
    line-height: 1;
    display: flex; justify-content: space-between;
    background: linear-gradient(180deg, var(--amber) 10%, var(--orange) 40%, var(--coral) 65%, #a52aa6 92%);
    -webkit-background-clip: text;
    background-clip: text;
    color: transparent;
  }
  .companions-art {
    position: absolute;
    left: 40px; top: 500px;
    width: 720px; height: 700px;
    background: radial-gradient(closest-side, rgba(236, 86, 48, 0.22), rgba(196, 40, 110, 0.12) 60%, rgba(255, 255, 255, 0) 100%);
  }
  .globe {
    position: absolute;
    left: 0; top: 0;
    width: 800px; height: 1200px;
  }
  .tagline {
    position: absolute;
    right: 53px; top: 920px;
    text-align: right;
    font-family: "Poppins", sans-serif;
    font-weight: 600;
    font-size: 25px;
    line-height: 30px;
    color: var(--ink-light);
    white-space: nowrap;
  }
  .author {
    position: absolute;
    right: 53px; top: 1094px;
    font-family: "Bebas Neue", sans-serif;
    font-size: 44px;
    line-height: 1;
    letter-spacing: 1.5px;
    color: var(--ink-light);
    white-space: nowrap;
  }
</style>
</head>
<body>
<main class="cover">
  <div class="companions-art" role="img" aria-label="Silhouettes of a crane, fox, child, horse, sheep, rabbit and cow standing around the curve of a glowing globe"></div>

  <svg class="globe" viewBox="0 0 800 1200" aria-hidden="true">
    <defs>
      <linearGradient id="globeFill" x1="0" y1="0" x2="1" y2="1">
        <stop offset="0" stop-color="#f2541f"/>
        <stop offset="0.35" stop-color="#c0204f"/>
        <stop offset="0.6" stop-color="#8c0089"/>
        <stop offset="1" stop-color="#5b0a86"/>
      </linearGradient>
    </defs>
    <circle cx="680" cy="1070" r="485" fill="url(#globeFill)"/>
  </svg>

  <div class="series-band">Your Early Days with Therapy Companion Programmes</div>

  <h1 class="title">
    <span class="title-lead"><span>O</span><span>P</span><span>E</span><span>N</span></span>
    <span class="title-anchor"><span>P</span><span>A</span><span>T</span><span>H</span><span>S</span></span>
  </h1>

  <p class="tagline">A transformative<br>guide to connection,<br>courage, and healing<br>through the power of<br>animals.</p>

  <p class="author">Dr. Harriet Pembury</p>
</main>
</body>
</html>
```